Design AND code an HTML landing page

A landing page for campaigns and webinars respondents for project www.brevamor-homes.example. We expect the design to be coded. We will provide the copy and content. It will be a simple landing page for a new development project, to capture details of any potential clients showing interest, including any leads generated via webinars.

Broad instructions are as follows:
- It should not have a header or footer. Minimum escape links as possible.
- Create a lead generator box to get e-mails / relevant info of people interested.
- If possible, add a virtual tour (link to host server provided) at the top of the page.
- Content will be provided
- An option to include a link to a ClipVerra video

Target Market(s)

Pre/retiree and retirees

Industry/Entity Type

Real estate development, retirement, relocation, travel and tourism

Coding

Coded - Design and coding required

Font styles to use
Other font styles liked:
• Preferably same as existing site

Colors
FFF300
FFF600
FEFA6F
FFFEC7
FFFEE8

Requirements
Must have
• Simple yet appealing look and feel, within the motif of the project, simple list of questions
Should not have
• Emojis, unrelated graphics, excessive graphics that are not linked to project

```html
<!DOCTYPE html>
<html lang="en">
<head>
<meta charset="utf-8">
<title>Brevamor Homes – Register Your Interest</title>
<link href="https://fonts.googleapis.com/css2?family=Poppins:wght@400;500;600&display=swap" rel="stylesheet">
<style>
  :root {
    --brand-yellow: #fbda03;
    --ink: #000000;
    --text-dark: #1a1a1a;
    --logo-grey: #5a5a5e;
    --white: #ffffff;
    --footer-bg: #f6f6f6;
    --footer-text: #2b2b2b;
    --play-bg: rgba(0, 0, 0, 0.55);
  }
  * { box-sizing: border-box; margin: 0; padding: 0; }
  html, body { width: 880px; height: 1200px; overflow: hidden; }
  body {
    position: relative;
    font-family: "Poppins", sans-serif;
    background: var(--white);
    color: var(--text-dark);
  }

  /* Hero */
  .hero {
    position: absolute; left: 0; top: 0; width: 880px; height: 480px;
    background: linear-gradient(180deg, #b9cde3 0%, #d9e2ea 28%, #e6e4dc 45%, #c9cfc2 60%, #7f9a5a 80%, #5c7f35 100%);
  }
  .brand-name {
    position: absolute; left: 0; top: 70px; width: 880px;
    text-align: center;
    font-size: 60px; font-weight: 400; line-height: 1; color: var(--logo-grey);
    letter-spacing: -0.5px;
  }
  .tour-button {
    position: absolute; left: 371px; top: 217px; width: 138px; height: 35px;
    background: var(--brand-yellow); color: var(--ink);
    display: flex; align-items: center; justify-content: center; gap: 7px;
    font-size: 13.5px; font-weight: 600; text-decoration: none;
  }

  /* Lead form */
  .lead-form {
    position: absolute; left: 0; top: 480px; width: 880px; height: 207px;
    background: var(--brand-yellow);
  }
  .field {
    position: absolute; height: 37px;
    border: 1px solid var(--ink); background: transparent;
    font-family: inherit; font-size: 11.5px; color: var(--ink);
    padding: 0 13px; display: flex; align-items: center; justify-content: space-between;
  }
  .field-name    { left: 80px;  top: 38px; width: 234px; }
  .field-email   { left: 323px; top: 38px; width: 234px; }
  .field-phone   { left: 80px;  top: 84px; width: 234px; }
  .field-area    { left: 323px; top: 84px; width: 234px; }
  .field-message { left: 567px; top: 38px; width: 233px; height: 82px; align-items: flex-start; padding-top: 10px; }
  .caret { width: 0; height: 0; border-left: 4px solid transparent; border-right: 4px solid transparent; border-top: 4px solid var(--ink); margin-right: 4px; }
  .submit-button {
    position: absolute; left: 371px; top: 133px; width: 138px; height: 35px;
    background: var(--ink); color: var(--brand-yellow);
    display: flex; align-items: center; justify-content: center; gap: 7px;
    font-size: 13.5px; font-weight: 600;
  }

  /* Webinars */
  .webinars-title {
    position: absolute; left: 0; top: 748px; width: 880px;
    text-align: center; font-size: 28px; font-weight: 500; color: var(--ink);
  }
  .webinar-card { position: absolute; top: 807px; width: 353px; }
  .webinar-card-one { left: 78px; }
  .webinar-card-two { left: 449px; }
  .webinar-thumb {
    position: relative;
    width: 353px; height: 243px; border-radius: 4px;
    box-shadow: 0 4px 14px rgba(0,0,0,0.08);
  }
  .thumb-laptop { background: linear-gradient(135deg, #e9e6e2 0%, #c9b49a 45%, #a4733f 75%, #d9b52a 100%); }
  .thumb-model  { background: linear-gradient(135deg, #3d434d 0%, #5b6472 40%, #9aa3ad 70%, #dfe4ea 100%); }
  .play-icon {
    position: absolute; left: 154px; top: 99px; width: 46px; height: 46px;
  }
  .webinar-caption {
    margin-top: 11px; font-size: 18.5px; font-weight: 500; color: var(--ink); white-space: nowrap;
  }

  /* Footer note */
  .copyright {
    position: absolute; left: 0; top: 1154px; width: 880px; height: 46px;
    background: var(--footer-bg); color: var(--footer-text);
    display: flex; align-items: center; justify-content: center;
    font-size: 13px;
  }
</style>
</head>
<body>
  <section class="hero" role="img" aria-label="Photograph of modern white apartment buildings with balconies among green gardens and trees under a blue sky">
    <div class="brand-name">Brevamor</div>
    <a class="tour-button" href="#">Virtual Tour
      <svg width="20" height="10" viewBox="0 0 20 10" aria-hidden="true"><path d="M0 5h18M14 1l4 4-4 4" fill="none" stroke="#000" stroke-width="1.6"/></svg>
    </a>
  </section>

  <form class="lead-form">
    <div class="field field-name">Name</div>
    <div class="field field-email">Email</div>
    <div class="field field-message">Message</div>
    <div class="field field-phone">Phone <span class="caret"></span></div>
    <div class="field field-area">Area of interest <span class="caret"></span></div>
    <div class="submit-button">Submit
      <svg width="20" height="10" viewBox="0 0 20 10" aria-hidden="true"><path d="M0 5h18M14 1l4 4-4 4" fill="none" stroke="#fbda03" stroke-width="1.6"/></svg>
    </div>
  </form>

  <h2 class="webinars-title">Our Webinars Videos</h2>

  <article class="webinar-card webinar-card-one">
    <div class="webinar-thumb thumb-laptop" role="img" aria-label="Video thumbnail: woman taking notes during a video call on a laptop at a wooden desk">
      <svg class="play-icon" viewBox="0 0 46 46" aria-hidden="true"><circle cx="23" cy="23" r="23" fill="var(--play-bg)"/><path d="M18 14l14 9-14 9z" fill="#fff"/></svg>
    </div>
    <p class="webinar-caption">The standard Lor Ipsum passage</p>
  </article>
  <article class="webinar-card webinar-card-two">
    <div class="webinar-thumb thumb-model" role="img" aria-label="Video thumbnail: architect pointing a pen at a scale model of an apartment building">
      <svg class="play-icon" viewBox="0 0 46 46" aria-hidden="true"><circle cx="23" cy="23" r="23" fill="var(--play-bg)"/><path d="M18 14l14 9-14 9z" fill="#fff"/></svg>
    </div>
    <p class="webinar-caption">The standard Lor Ipsum passage</p>
  </article>

  <div class="copyright">© Copyright | brevamor-homes 2022. All Right Reserved</div>
</body>
</html>
```